Kelvane Plumbing Business cards

Company is Kelvane Plumbing.
name Dashel Morrowby, I am a plumber, drainer, gasfitter and roofer
Mobile: 0431 906 154
Email address: info@kelvaneplumbing.example (check out my website for some ideas)
Website: www.kelvaneplumbing.example
ABN: 82 916 203 471
LIC: 604517K

I am reliable all round plumber. I am a 24 hour emergency service. Kelvane Plumbing is a professional plumbing service in the Illawarra, South Coast, Southern Sydney and Southern Highland regions of NSW. We offer a 24 hour emergency service for piece of mind to our customers. Call us now to see how we can help you. Kelvane Plumbing approaches every job with attention to detail and excellent customer service. With our superior workmanship you can be confident that the job will be done right the first time around. You can rest assured with results that are guaranteed to last.

Target Market(s)

the general public

Contact Information for Business Card

look up website for some ideas something with similar colours to logo and new modern and to catch the eye.

Colors
fdfdfd
ffffff
000000
7f7f7f
aaaaaa
33a6d7
0492cd

Requirements
Must have
• all contact details
• company- Kelvane Plumbing
• name- Dashel Morrowby
• number mobile- 0431 906 154
• Email address- info@kelvaneplumbing.example
• Website- www.kelvaneplumbing.example
• ABN- 82 916 203 471
• LIC- 604517K

```html
<!DOCTYPE html>
<html lang="en">
<head>
<meta charset="utf-8">
<title>Kelvane Plumbing — Business Cards</title>
<link href="https://fonts.googleapis.com/css2?family=Montserrat:wght@500;600&family=Open+Sans:wght@400&display=swap" rel="stylesheet">
<style>
  :root {
    --stage-light: #e8e9eb;
    --stage-dark: #cfd0d2;
    --card-dark-a: #242426;
    --card-dark-b: #3b3b3e;
    --brand-blue: #0492cd;
    --brand-grey: #7f7f7f;
    --text-light: #ffffff;
    --text-soft: #e6e6e6;
    --text-muted: #aaaaaa;
    --paper: #ffffff;
  }
  * { margin: 0; padding: 0; box-sizing: border-box; }
  html, body { width: 799px; height: 1200px; overflow: hidden; }
  body {
    position: relative;
    background: radial-gradient(ellipse at 50% 50%, var(--stage-light) 0%, var(--stage-dark) 75%);
    font-family: "Open Sans", sans-serif;
  }
  .card {
    position: absolute;
    left: 148px;
    width: 504px;
    height: 288px;
    overflow: hidden;
  }
  .card-front {
    top: 170px;
    border-radius: 13px;
    background: linear-gradient(90deg, var(--card-dark-a) 0%, var(--card-dark-b) 100%);
  }
  .card-back {
    top: 703px;
    background: var(--paper);
  }
  .brand-mark {
    position: absolute;
    display: flex;
    align-items: center;
    gap: 8px;
    font-family: "Montserrat", sans-serif;
    font-weight: 600;
    color: var(--brand-blue);
    white-space: nowrap;
  }
  .brand-mark .dot {
    border-radius: 50%;
    background: var(--brand-grey);
    flex: none;
  }
  .card-front .brand-mark { left: 32px; top: 60px; font-size: 17px; }
  .card-front .brand-mark .dot { width: 24px; height: 24px; }
  .brand-faint {
    position: absolute;
    right: 16px;
    top: 252px;
    font-family: "Montserrat", sans-serif;
    font-weight: 600;
    font-size: 17px;
    color: rgba(255,255,255,0.1);
    white-space: nowrap;
  }
  .holder-name {
    position: absolute;
    left: 34px;
    top: 148px;
    font-family: "Montserrat", sans-serif;
    font-weight: 600;
    font-size: 22px;
    line-height: 1;
    color: var(--text-light);
  }
  .holder-role {
    position: absolute;
    left: 34px;
    top: 174px;
    font-family: "Montserrat", sans-serif;
    font-weight: 500;
    font-size: 11.5px;
    color: var(--text-soft);
  }
  .contact {
    position: absolute;
    display: flex;
    align-items: center;
    gap: 8px;
    font-size: 12px;
    color: var(--text-light);
    white-space: nowrap;
  }
  .contact svg { width: 9px; height: 9px; fill: var(--text-soft); flex: none; }
  .contact-phone { left: 35px; top: 199px; }
  .contact-email { left: 170px; top: 199px; }
  .contact-web { left: 35px; top: 220px; }
  .rule {
    position: absolute;
    left: 31px;
    top: 243px;
    width: 371px;
    height: 1px;
    background: linear-gradient(90deg, var(--brand-grey), var(--brand-blue));
  }
  .registration {
    position: absolute;
    left: 35px;
    top: 253px;
    font-size: 11px;
    color: var(--text-muted);
    white-space: nowrap;
  }
  .registration span + span { margin-left: 18px; }
  .card-back .brand-mark {
    left: 50%;
    top: 50%;
    transform: translate(-50%, -50%);
    font-size: 30px;
    gap: 14px;
  }
  .card-back .brand-mark .dot { width: 36px; height: 36px; }
</style>
</head>
<body>
  <section class="card card-front">
    <div class="brand-mark"><span class="dot"></span>Kelvane Plumbing</div>
    <div class="brand-faint">Kelvane Plumbing</div>
    <h1 class="holder-name">Dashel Morrowby</h1>
    <p class="holder-role">Plumber, Drainer, Gasfitter, Roofer</p>
    <div class="contact contact-phone">
      <svg viewBox="0 0 10 10"><path d="M2 0.5 L3.6 2.6 L2.8 3.6 Q3.6 5.6 6.4 7.2 L7.4 6.4 L9.5 8 L8.4 9.5 Q1 8 0.5 1.6 Z"/></svg>
      <span>0431 906 154</span>
    </div>
    <div class="contact contact-email">
      <svg viewBox="0 0 10 10"><rect x="0.5" y="2" width="9" height="6"/></svg>
      <span>info@kelvaneplumbing.example</span>
    </div>
    <div class="contact contact-web">
      <svg viewBox="0 0 10 10"><circle cx="5" cy="5" r="4.5"/></svg>
      <span>www.kelvaneplumbing.example</span>
    </div>
    <div class="rule"></div>
    <p class="registration"><span>ABN 82 916 203 471</span><span>LIC 604517K</span></p>
  </section>

  <section class="card card-back">
    <div class="brand-mark"><span class="dot"></span>Kelvane Plumbing</div>
  </section>
</body>
</html>
```